A new PowerPoint Template for a French consulting company

Who are we?

Formed in 2005, Brevane is a consulting company specialising in the human aspect of change and transformation.

From our offices in the heart of Paris, our team of 30 consultants work with leading organisations in the Aerospace, Finance, Transportation and Public sectors to deliver lasting change.

Our customers trust us with some of their most strategic and sensitive projects. They trust us with these projects because:
- We listen to them, ensuring we understand the real needs of their business
- We involve them, co-developing and tailoring our solutions to the specific challenges they face
- We’re professional, without taking ourselves too seriously
- We’re imaginative, whilst always remaining pragmatic
- We get results!

You can find out more about who we are and the work we do here: http://www.brevane-conseil.fr/en

What we need from you?

We’re approaching our 10th birthday and, whilst we still love what we do, we think it’s the right time to update our image.

We’d like you to design us a new PowerPoint template, that will be used for all of our internal and client facing work. You can base your submissions on our existing logo and colour scheme (see files attached) or you can submit your own fresh ideas – after all, we’re not afraid of change!

Finally, whilst we’re looking for you to be creative, there are some simple guidelines that we need you to keep in mind:

1. The Template needs to include both a front cover and a “content” page

2. The front cover needs to:
- Include our logo
- Reflect “who we are” and the type of work that we do

3. The content page needs to:
- Have a predominantly white background
- Be practical to use, making an effective use of the 4:3 standard PPT size
- Include an area across the top of the page for the slide title
- Include areas along the bottom of the page for the page number and date

4. If you decide to propose a new colour scheme, it should be balanced and the “accents” usable

5. The PowerPoint Template needs to be “printer friendly”

6. The fonts you use should be standard

What we don’t want?

To give you as much help as possible, here are some things that we really don’t want:

- Submissions that are dull grey or navy blue, suggesting we’re nothing but boring corporate suits
- Submissions that are Barbie pink or too “soft and cuddly”
- Submissions that use lots of stock images of “happy, smiling, consultants”
- Submissions that will be the height of fashion today, but completely out of date next year

Industry/Entity Type

It Company

```html
<!DOCTYPE html>
<html lang="en">
<head>
<meta charset="UTF-8">
<title>Brevane – About Us</title>
<link href="https://fonts.googleapis.com/css2?family=Carlito:wght@400;700&display=swap" rel="stylesheet">
<style>
  :root {
    --plum: #6b0f3e;
    --teal: #2fb5a8;
    --ink: #3d3d3d;
    --text: #1f1f1f;
    --paper: #ffffff;
    --sky: #b9d6ee;
    --facade: #c7b49a;
  }
  * { margin: 0; padding: 0; box-sizing: border-box; }
  html, body {
    width: 1200px; height: 900px; overflow: hidden;
    background: var(--paper);
    font-family: "Carlito", Calibri, sans-serif;
    color: var(--text);
  }
  .slide { position: relative; width: 1200px; height: 900px; }

  .top-rule { position: absolute; top: 0; left: 0; width: 1200px; height: 7px; display: flex; gap: 3px; }
  .top-rule .plum { width: 600px; background: var(--plum); }
  .top-rule .teal { flex: 1; background: var(--teal); }

  .brand {
    position: absolute; left: 63px; top: 34px;
    font-size: 44px; font-weight: 700; line-height: 1;
    color: var(--plum);
  }

  .slide-title {
    position: absolute; left: 63px; top: 156px;
    font-size: 47px; font-weight: 700; line-height: 1; color: var(--ink); letter-spacing: 0.3px;
  }
  .intro {
    position: absolute; left: 63px; top: 243px;
    font-size: 22px; line-height: 30px; color: var(--text); white-space: nowrap;
  }

  .column { position: absolute; top: 436px; width: 380px; }
  .column.first { left: 63px; }
  .column.second { left: 480px; }
  .column h2 {
    display: flex; align-items: center; gap: 16px;
    font-size: 23.5px; font-weight: 700; line-height: 1; color: var(--ink);
  }
  .column h2 svg { width: 23px; height: 23px; fill: var(--ink); }
  .column p {
    margin-top: 26px;
    font-size: 17px; line-height: 23.3px; color: var(--text); white-space: nowrap;
  }

  .photo {
    position: absolute; left: 862px; top: 428px; width: 255px; height: 328px;
    background: linear-gradient(180deg, var(--sky) 0%, #d9d2c4 30%, var(--facade) 65%, #8e9a7e 100%);
  }

  .page-number {
    position: absolute; left: 1116px; top: 844px; width: 36px; height: 32px;
  }
  .page-number svg { position: absolute; inset: 0; }
  .page-number span {
    position: absolute; left: 0; top: 0; width: 28px; height: 32px;
    display: flex; align-items: center; justify-content: center;
    color: var(--paper); font-size: 17px;
  }
</style>
</head>
<body>
<main class="slide">
  <div class="top-rule"><div class="plum"></div><div class="teal"></div></div>

  <header class="brand">Brevane</header>

  <h1 class="slide-title">ABOUT US</h1>

  <p class="intro">Lorem ipsum dolor sit amet, consectetur adipiscing elit, sed do eiusmod tempor incididunt ut labore et<br>dolore magna aliqua. Ut enim ad minim veniam, quis nostrud exercitation ullamco laboris nisi ut<br>aliquip ex ea commodo consequat. Duis aute irure dolor in reprehenderit in voluptate velit esse cillum<br>dolore eu fugiat nulla pariatur. Excepteur sint occaecat cupidatat non proident, sunt in culpa qui officia<br>deserunt mollit anim id est laborum</p>

  <section class="column first">
    <h2>Section 1.10.32
      <svg viewBox="0 0 24 24" aria-hidden="true"><path d="M2 5h7l2 2h11v13H2z"/></svg>
    </h2>
    <p>Sed ut perspiciatis unde omnis iste natus<br>error sit voluptatem accusantium dolor-<br>emque laudantium, totam rem aperiam,<br>eaque ipsa quae ab illo inventore veritatis et<br>quasi architecto beatae vitae dicta sunt<br>explicabo.</p>
  </section>

  <section class="column second">
    <h2>Section 1.10.32
      <svg viewBox="0 0 24 24" aria-hidden="true"><path d="M6 2h2v3H6zM16 2h2v3h-2zM3 4h18v18H3zM5 9v11h14V9z"/></svg>
    </h2>
    <p>Sed ut perspiciatis unde omnis iste natus<br>error sit voluptatem accusantium dolor-<br>emque laudantium, totam rem aperiam,<br>eaque ipsa quae ab illo inventore verita-<br>tis et quasi architecto beatae vitae dicta<br>sunt explicabo.</p>
  </section>

  <div class="photo" role="img" aria-label="Modern office building with stone and glass facade under a clear blue sky"></div>

  <div class="page-number">
    <svg viewBox="0 0 36 32" aria-hidden="true"><path d="M0 0H24L36 16L24 32H0z" fill="var(--plum)"/></svg>
    <span>1</span>
  </div>
</main>
</body>
</html>
```